New Web Design Project

We are working with RT Aggregates (https://ridgetopaggregates.example) and are seeking a website design that reflects a modern, professional, and industry-appropriate aesthetic. Here’s some details on what we’re looking for on the website redesign.
Home page:
Our video playing - with numbers rolling for totals:
drivers, tons hauled, miles of roads paved, dirt moved, rock hauled
Competitor & Inspiration Sites:
(We will include links to competitor or inspirational websites to help guide your creative direction.)
lumdaxo.example - Transitions
brisklane.example - Color contrasts & dynamic logo
quorvane.example - Dynamic tabs
⸻
About Us & How We Work
Thank you for taking the time to consider designing a website for us. We are a web development agency based in Stockton, California (USA). Most of our projects follow a consistent process, and understanding how we work may help increase your chances of being selected.
All websites are custom-coded in-house. While there are no restrictions on the tools you use to design, Figma files are preferred.
⸻
Our Design Selection Process
Designs that meet our quality standards may be marked as four-star designs. These designs are presented to the client, who selects the final concept we move forward with.
Once a design reaches this stage, it may also be reused as inspiration or presented to future clients. This means your design can have multiple opportunities to sell, even beyond the original project.
To improve your chances of success, please follow the guidelines below.
⸻
Image & Icon Usage
If you include images or icons in your design, please provide a link to the source so we can purchase the asset.
• Stock imagery is encouraged.
• Focus on conveying the mood, tone, and personality of the brand.
• You may use any royalty-free image provider., but we primarily use Pexora Images, but we are open to purchasing assets from other platforms.
⸻
Fonts
Please identify the fonts used in your design (a message is sufficient).
• We only use Google Fonts and Adobe Fonts.
• Clean, legible typography is strongly preferred.
⸻
Content Guidelines
We welcome creative ideas and layout suggestions.
• Stock images are commonly used to communicate the design vision.
• Client-specific photography is often added after launch.
• Lorem Ipsum is acceptable for paragraph text.
• Please write real, properly written English headings so we can clearly understand section intent and structure.
⸻
Inspiration
We typically include a few reference websites in the brief to help establish visual direction. These are meant as inspiration—not templates.
⸻
Revisions
We rarely request design revisions.
• If we see a concept that may not resonate with the client, we may ask for clarification or adjustment.
• Minor refinements are typically handled during the development phase rather than the design phase.
⸻
Feedback
Due to the volume of projects we manage, we generally do not provide ongoing feedback during the design process.
• Well-thought-out questions that are specific and actionable may receive a response.
• General requests such as “feedback, please” typically go unanswered.
⸻
Client Communication
All communication regarding this project must remain within PitchHive and with our team only.
• Designers may not contact the client directly under any circumstances.
• If a designer reaches out to the client outside of PitchHive and we become aware of it, the incident will be reported to PitchHive.
• To protect both the client and the integrity of the design process, we often use placeholder or internal brand names when launching design projects.
This policy is non-negotiable and helps ensure a fair, professional, and organized process for everyone involved.

```html
<!DOCTYPE html>
<html lang="en">
<head>
<meta charset="utf-8">
<title>RT Aggregates — Home Layout</title>
<link rel="stylesheet" href="https://fonts.googleapis.com/css2?family=Inter:wght@400;500;600;700;800&family=Rubik:wght@700;800&display=swap">
<style>
  :root {
    --header-grey: #8b8b8b;
    --hero-grey: #e3e3e3;
    --page-white: #ffffff;
    --ink: #1d1d22;
    --note-red: #8c0a1c;
    --note-yellow: #ffee00;
    --accent-orange: #f07025;
    --logo-white: #ffffff;
    --video-black: #000000;
  }
  * { box-sizing: border-box; margin: 0; padding: 0; }
  html, body { width: 1200px; height: 645px; overflow: hidden; background: var(--page-white); }
  body { position: relative; font-family: "Inter", sans-serif; color: var(--ink); }

  .site-header {
    position: absolute; left: 0; top: 0; width: 1200px; height: 53px;
    background: var(--header-grey);
  }
  .brand {
    position: absolute; left: 96px; top: 18px;
    font-family: "Inter", sans-serif; font-weight: 700; font-size: 13px;
    color: var(--logo-white); letter-spacing: -0.2px;
  }
  .main-nav { position: absolute; top: 20px; left: 0; width: 1200px; }
  .main-nav a {
    position: absolute; font-size: 9.5px; font-weight: 500; letter-spacing: 0.5px;
    color: #fff; text-decoration: underline; text-underline-offset: 2px;
  }
  .note {
    font-family: "Rubik", sans-serif; font-weight: 800; color: var(--note-red);
    position: absolute; white-space: nowrap;
  }
  .note-title { left: 583px; top: 5px; transform: translateX(-50%); font-size: 12px; letter-spacing: 0.1px; }
  .note-menu { left: 476px; top: 27px; font-size: 9.5px; }
  .note-arrows { position: absolute; left: 250px; top: 24px; }

  .hero {
    position: absolute; left: 0; top: 53px; width: 1200px; height: 461px;
    background: var(--hero-grey);
  }
  .hero-video {
    position: absolute; left: 51px; top: 0; width: 708px; height: 411px;
    background: radial-gradient(ellipse at 50% 60%, #2a0707 0%, var(--video-black) 65%);
    box-shadow: 0 -4px 8px rgba(0,0,0,0.35);
  }
  .note-video {
    color: var(--note-yellow); font-size: 12px;
    left: 348px; top: 78px; transform: translateX(-50%);
  }
  .hero-copy { position: absolute; left: 794px; top: 0; width: 300px; }
  .note-head { position: relative; display: block; font-size: 12px; margin: 107px 0 0 4px; }
  .hero-title {
    margin-top: 14px; font-size: 24.5px; font-weight: 600; line-height: 29px; letter-spacing: -0.2px;
  }
  .hero-lede { margin-top: 13px; font-size: 10px; line-height: 16.5px; width: 235px; }
  .hero-cta {
    display: block; margin-top: 15px; width: 238px; height: 34px;
    background: var(--accent-orange); color: #fff; font-size: 10px; font-weight: 600;
    line-height: 34px; padding-left: 18px; text-decoration: none;
  }

  .stats { position: absolute; left: 0; top: 514px; width: 1200px; height: 131px; background: var(--page-white); }
  .stat-figure {
    position: absolute; top: 45px; transform: translateX(-50%);
    font-size: 27px; font-weight: 700; letter-spacing: -0.3px;
  }
</style>
</head>
<body>
  <header class="site-header">
    <span class="note note-title">Annotated layout Explaining Section Structure &nbsp;and responsiveness - Part 1</span>
    <div class="brand">RT Aggregates</div>
    <svg class="note-arrows" width="540" height="14" viewBox="0 0 540 14" aria-hidden="true">
      <g fill="none" stroke="#8c0a1c" stroke-width="2">
        <path d="M41 3 H10 V0.5 L3 7 L10 13.5 V11 H41 Z" fill="none"/>
        <path d="M50 7 H218" stroke-width="2.5"/>
        <path d="M333 7 H480" stroke-width="2.5"/>
        <path d="M483 3 H522 V0.5 L535 7 L522 13.5 V11 H483 Z"/>
      </g>
    </svg>
    <span class="note note-menu">Logo &amp; Menu bar</span>
    <nav class="main-nav">
      <a href="#" style="left:802px">HOME</a>
      <a href="#" style="left:854px">ABOUT</a>
      <a href="#" style="left:911px">SERVICES</a>
      <a href="#" style="left:981px">CAREERS</a>
      <a href="#" style="left:1049px">CONTACT</a>
    </nav>
  </header>

  <section class="hero">
    <div class="hero-video" role="img" aria-label="Hero video area: looping company reel with glowing title artwork on black">
      <span class="note note-video">Place for Video</span>
    </div>
    <div class="hero-copy">
      <span class="note note-head">Place for Head Content</span>
      <h1 class="hero-title">Building California’s Infrastructure,<br>One Load at a Time</h1>
      <p class="hero-lede">Reliable materials. Proven logistics. Statewide impact.</p>
      <a class="hero-cta" href="#">Explore Our Work</a>
    </div>
  </section>

  <section class="stats">
    <div class="stat-figure" style="left:157px">2500</div>
    <div class="stat-figure" style="left:449px">15,380,000</div>
    <div class="stat-figure" style="left:742px">4200</div>
    <div class="stat-figure" style="left:1035px">50</div>
  </section>
</body>
</html>
```